Beatrices Business Card

Looking for business card that is PROFESSIONAL yet has a flair of design. My colors are white with black font. My last name is Halloway so a tiara could be faded in the background OR embossed. I would love my pic to be in a frame with an interesting background/texture. Fonts need to be CLASSY, not cheesy. I need ALL verbiage included but can be on both back and front.

Beatrice Halloway
Real Estate Agent
720-555-0193 bhalloway@velmora.net

Accredited Highland Terrain Advisor
Accredited Premier Dwelling Promotion Advisor
Accredited Settlement Adept

Velora Keystone
41726 Driftwood Blvd 303-555-014 Each office indepdendly owned and operated

Target Market(s)

Sellers and Buyers. Millennials on up

Industry/Entity Type

Real Estate Agent

Contact Information for Business Card

Beatrice Halloway
Real Estate Agent

Velora Keystone
41726 Driftwood Blvd 303-555-014
Each office independently owned and operated

Font styles to use
Serif

Colors
f04a50
ffffff
000000

Requirements
Must have
• a classy, fun feel to it. Unique, high end. But it has to look professional and be taken seriously.
Nice to have
• Elegant, classy, fun.
Should not have
• anything cheesy or tacky.

```html
<!DOCTYPE html>
<html lang="en">
<head>
<meta charset="utf-8">
<title>Beatrice Halloway – Business Card</title>
<link href="https://fonts.googleapis.com/css2?family=Cinzel:wght@400;700&display=swap" rel="stylesheet">
<style>
  :root {
    --page: #ecebe8;
    --card-white: #ffffff;
    --card-red: #c8102e;
    --ink: #111111;
    --ink-soft: #222222;
    --texture: #f1f1f2;
    --tiara-gold: #d9bf7a;
    --tiara-light: #efe0b0;
    --photo-light: #f2f2f2;
    --photo-warm: #b0623d;
    --photo-red: #c41a22;
  }
  * { box-sizing: border-box; margin: 0; padding: 0; }
  html, body {
    width: 1200px; height: 800px; overflow: hidden;
    background: var(--page);
    font-family: "Cinzel", "Trajan Pro", serif;
  }
  .stage {
    width: 1200px; height: 800px;
    display: flex; align-items: center; justify-content: center; gap: 60px;
  }
  .card {
    width: 525px; height: 300px;
    position: relative; overflow: hidden;
    box-shadow: 0 6px 18px rgba(0,0,0,.18);
  }

  /* back */
  .card-back { background: var(--card-red); }
  .card-back__top {
    height: 108px; background: var(--card-white);
    display: flex; align-items: center; justify-content: center;
  }
  .tiara {
    width: 64px; height: 44px; border-radius: 6px 6px 3px 3px;
    background: linear-gradient(180deg, var(--tiara-light), var(--tiara-gold));
  }
  .card-back__body {
    color: var(--card-white); text-align: center;
    padding-top: 26px; font-size: 12.5px; line-height: 1.45;
  }
  .credentials { margin-bottom: 14px; }
  .brokerage { font-weight: 700; font-size: 15px; margin-bottom: 12px; }

  /* front */
  .card-front {
    background: var(--texture);
    display: flex;
  }
  .portrait {
    width: 260px; height: 100%;
    background: linear-gradient(180deg, var(--photo-light) 0%, var(--photo-warm) 45%, var(--photo-red) 100%);
  }
  .identity {
    flex: 1; display: flex; flex-direction: column; align-items: center;
    padding-top: 44px; color: var(--ink);
  }
  .name { font-weight: 700; font-size: 21px; letter-spacing: .5px; }
  .title { font-size: 14px; margin-top: 2px; color: var(--ink-soft); }
  .identity .tiara { margin: 34px 0 40px; width: 58px; height: 40px; }
  .contact { text-align: center; font-size: 13px; line-height: 1.45; }
</style>
</head>
<body>
<main class="stage">
  <section class="card card-back">
    <div class="card-back__top">
      <div class="tiara" role="img" aria-label="Gold jewelled tiara ornament"></div>
    </div>
    <div class="card-back__body">
      <p class="credentials">
        Accredited Highland Terrain Advisor<br>
        Accredited Premier Dwelling Promotion Advisor<br>
        Accredited Settlement Adept
      </p>
      <p class="brokerage">Velora Keystone</p>
      <p class="address">
        41726 Driftwood Blvd, Larchmere, CO 80499 · 303-555-014<br>
        Each office independently owned and operated
      </p>
    </div>
  </section>

  <section class="card card-front">
    <div class="portrait" role="img" aria-label="Portrait photo of Beatrice Halloway in a red top"></div>
    <div class="identity">
      <h1 class="name">Beatrice Halloway</h1>
      <p class="title">Real Estate Agent</p>
      <div class="tiara" role="img" aria-label="Gold jewelled tiara ornament"></div>
      <p class="contact">720-555-0193<br>bhalloway@velmora.net</p>
    </div>
  </section>
</main>
</body>
</html>
```